Letterhead to Prospective Clients

Create a letterhead (word & canva) that I will use to send letters to prospective clients and also include the Coralwood Estate Partners Logo, My Contact Details and Interchangeable "Suburb". Use the same font and colour pallete

Maris Dulworth | "Suburb" Specialist - Harbourline & Surrounds
Mobile: 0417 862 095
Email: MD@CoralwoodEstatePartners.com.au

```html
<!DOCTYPE html>
<html lang="en">
<head>
<meta charset="UTF-8">
<title>Coralwood Estate Partners – Letterhead</title>
<link href="https://fonts.googleapis.com/css2?family=Source+Sans+3:wght@300;400;700&display=swap" rel="stylesheet">
<style>
  :root {
    --navy: #363363;
    --tan: #cc9a68;
    --orange: #cb6636;
    --deep: #0e2a40;
    --gold: #c9973a;
    --ink: #16213e;
    --white: #ffffff;
  }
  html, body { margin: 0; padding: 0; overflow: hidden; background: var(--white); }
  .letterhead {
    position: relative;
    width: 855px;
    height: 1200px;
    overflow: hidden;
    background: var(--white);
    font-family: "Source Sans 3", "Myriad Pro", sans-serif;
  }
  .header-band {
    position: absolute;
    left: 172px; top: 46px;
    width: 683px; height: 20px;
    background: var(--navy);
  }
  .header-rule {
    position: absolute;
    left: 171px; top: 69px;
    width: 684px; height: 4px;
    background: var(--navy);
  }
  .header-accent {
    position: absolute;
    left: 0; top: 25px;
    width: 196px; height: 81px;
    background: linear-gradient(90deg, var(--tan) 0%, var(--navy) 55%, var(--tan) 100%);
  }
  .footer-band {
    position: absolute;
    left: 0; top: 1073px;
    width: 680px; height: 69px;
    background: var(--navy);
  }
  .footer-accent {
    position: absolute;
    left: 640px; top: 1040px;
    width: 215px; height: 134px;
    background: linear-gradient(90deg, var(--tan) 0%, var(--navy) 60%, var(--tan) 100%);
  }
  .brand {
    position: absolute;
    left: 520px;
    top: 92px;
    width: 300px;
    text-align: center;
    font-weight: 300;
  }
  .brand-name { color: var(--ink); font-size: 37px; letter-spacing: 6px; line-height: 1; }
  .brand-sub { color: var(--tan); font-size: 10px; font-weight: 400; letter-spacing: 3.5px; margin-top: 19px; }
  .recipient { position: absolute; left: 116px; top: 243px; }
  .recipient-label { color: var(--ink); font-size: 15px; line-height: 18px; }
  .recipient-name { color: var(--gold); font-weight: 700; font-size: 19px; line-height: 22px; }
  .contact-icon {
    position: absolute;
    width: 40px; height: 40px;
    margin: -20px 0 0 -20px;
  }
  .contact-text {
    position: absolute;
    color: var(--white);
    font-size: 12.5px;
    line-height: 17px;
    text-align: center;
    white-space: nowrap;
    transform: translateX(-50%);
  }
</style>
</head>
<body>
<div class="letterhead">
  <div class="header-accent" role="img" aria-label="Decorative folded ribbon accent in tan and navy"></div>
  <div class="header-band"></div>
  <div class="header-rule"></div>

  <div class="brand">
    <div class="brand-name">CORALWOOD</div>
    <div class="brand-sub">ESTATE PARTNERS</div>
  </div>

  <div class="recipient">
    <div class="recipient-label">To,</div>
    <div class="recipient-name">DEVON ASHCROFT</div>
  </div>

  <div class="footer-band"></div>
  <div class="footer-accent" role="img" aria-label="Decorative folded ribbon accent in tan and navy"></div>

  <svg class="contact-icon" style="left:166px;top:1073px" viewBox="0 0 40 40" aria-hidden="true">
    <circle cx="20" cy="20" r="20" fill="var(--deep)"/>
    <circle cx="20" cy="20" r="16.5" fill="var(--white)"/>
    <circle cx="20" cy="20" r="14.5" fill="var(--tan)"/>
    <path fill="var(--deep)" d="M15.5,13.5 l2.2,-0.6 1.3,3 -1.4,1.1 q1,2.4 3.3,3.6 l1.2,-1.3 3,1.4 -0.6,2.2 q-4.2,0.6 -7.1,-2.6 q-2.7,-3 -1.9,-6.8 Z"/>
    <path fill="none" stroke="var(--deep)" stroke-width="0.9" d="M21,13.5 a4,4 0 0 1 3.5,3.5 M21.4,11.5 a6,6 0 0 1 5.1,5.1"/>
  </svg>
  <div class="contact-text" style="left:166px;top:1107px">0417 862 095</div>

  <svg class="contact-icon" style="left:326px;top:1073px" viewBox="0 0 40 40" aria-hidden="true">
    <circle cx="20" cy="20" r="20" fill="var(--deep)"/>
    <circle cx="20" cy="20" r="16.5" fill="var(--white)"/>
    <circle cx="20" cy="20" r="14.5" fill="var(--tan)"/>
    <g fill="none" stroke="var(--deep)" stroke-width="1">
      <circle cx="20" cy="20" r="6"/>
      <ellipse cx="20" cy="20" rx="2.6" ry="6"/>
      <path d="M14,20 H26 M15,17 H25 M15,23 H25"/>
    </g>
  </svg>
  <div class="contact-text" style="left:326px;top:1107px">MD@CoralwoodEstatePartners.com.au</div>

  <svg class="contact-icon" style="left:508px;top:1073px" viewBox="0 0 40 40" aria-hidden="true">
    <circle cx="20" cy="20" r="20" fill="var(--deep)"/>
    <circle cx="20" cy="20" r="16.5" fill="var(--white)"/>
    <circle cx="20" cy="20" r="14.5" fill="var(--tan)"/>
    <path fill="var(--deep)" d="M20,12.5 a5,5 0 0 1 5,5 c0,3.6 -5,9.5 -5,9.5 s-5,-5.9 -5,-9.5 a5,5 0 0 1 5,-5 Z"/>
    <circle cx="20" cy="17.5" r="1.8" fill="var(--tan)"/>
  </svg>
  <div class="contact-text" style="left:537px;top:1092px">Maris Dulworth | "Suburb"<br>Specialist - Harbourline &amp; Surrounds</div>
</div>
</body>
</html>
```